Joomla Template Design

Wellvane.com is a web hosting company that serves the Christian church industry. We need a new template designed that we can offer our customers through our hosting interface.

The template needs to be designed in Joomla 2.5 or higher. If you can create it in Artisteer it's a plus, but not required.

The template should also include plug-ins for:

Photo / Video Gallery
Calender
Donations
Form Creator (for contact us type forms)
Site Search
Social Media Links

A general style sample is attached as a guide. The style should be clean and simple.

When the template is complete, it should be sent with 3 color palettes (blue, green, grey) and include all graphics.

Target Market(s)

This template will be used primarily for churches and ministries.

Industry/Entity Type

Church

Requirements
Must have
• The template must include home and interior page designs.
Nice to have
• We prefer the design be made with artisteer (see pagelume.com), but it's not required.

```html
<!DOCTYPE html>
<html lang="en">
<head>
<meta charset="utf-8">
<title>Church Template – Home</title>
<link rel="stylesheet" href="https://fonts.googleapis.com/css2?family=Noto+Sans:wght@400;700&display=swap">
<style>
:root{
  --bg-light:#e0eacd;
  --bg-band:#a9c27a;
  --bg-band-dark:#8fae5d;
  --btn-top:#6f8d3a;
  --btn-bottom:#3f5a1c;
  --btn-edge:#b9cf92;
  --panel:#ffffff;
  --panel-edge:#c9c2a8;
  --box-edge:#c8c8c8;
  --heading-blue:#2b5d8c;
  --link-blue:#2f7bb8;
  --text:#111111;
  --muted:#4a4a4a;
  --head-text:#e2ead2;
  --placeholder-sky:#3f87d6;
  --placeholder-wood:#8a6a4a;
}
*{box-sizing:border-box;margin:0;padding:0}
html,body{width:1200px;height:1141px;overflow:hidden}
body{
  position:relative;
  font-family:"Noto Sans",Tahoma,sans-serif;
  color:var(--text);
  background:linear-gradient(to bottom,var(--bg-band-dark) 0,var(--bg-band) 42px,#c6d8a4 44px,var(--bg-light) 170px,var(--bg-light) 1068px,#c4d7a0 1070px,var(--bg-band) 1141px);
}
.main-nav{position:absolute;left:137px;top:4px;display:flex;gap:10px}
.nav-item{
  height:34px;padding:0 17px;display:flex;align-items:center;
  color:#fff;font-size:13.5px;text-decoration:none;
  background:linear-gradient(var(--btn-top),var(--btn-bottom));
  border:1px solid var(--btn-edge);border-top:none;border-radius:0 0 3px 3px;
}
.site-emblem{position:absolute;left:137px;top:48px;width:108px;height:108px;
  background:linear-gradient(135deg,#b08a62,var(--placeholder-wood) 55%,#d9d2c0);border-radius:6px}
.site-title{position:absolute;left:245px;top:76px;font-size:34px;font-weight:700;font-variant:small-caps;letter-spacing:1px;color:#000;line-height:1.2}
.site-slogan{position:absolute;left:420px;top:122px;font-size:14px;font-variant:small-caps;color:#000}
.site-search{position:absolute;left:806px;top:104px;width:241px;height:26px;background:#fff;border:1px solid #cfd6c2;border-radius:3px}
.site-search svg{position:absolute;right:6px;top:5px}
.page-panel{position:absolute;left:117px;top:156px;width:960px;height:914px;background:var(--panel);border:1px solid var(--panel-edge);border-bottom:none;border-radius:5px 5px 0 0}
.content-box{position:absolute;left:139px;top:178px;width:648px;height:880px;border:1px solid var(--box-edge);border-radius:4px;font-size:12.6px;line-height:17px}
.section-title{font-size:20px;line-height:26px;font-variant:small-caps;font-weight:400;color:var(--heading-blue);text-align:center;letter-spacing:.5px}
.col-who{position:absolute;left:16px;top:16px;width:298px}
.hero-image{display:block;margin:18px auto 0;width:212px;height:158px;border:3px solid #2a5d97;
  background:linear-gradient(to bottom,#1c5cb8,var(--placeholder-sky) 45%,#e9f1fb)}
.col-who h3{font-size:13.5px;margin-top:30px;line-height:17px}
.col-who p{margin-top:12px}
.btn{display:inline-flex;align-items:center;justify-content:center;width:103px;height:31px;color:#fff;font-size:11.5px;font-weight:700;text-decoration:none;
  background:linear-gradient(var(--btn-top),var(--btn-bottom));border:1px solid var(--btn-edge);border-radius:3px;box-shadow:0 1px 2px rgba(0,0,0,.25)}
.col-who .btn{margin-top:11px}
.col-feed{position:absolute;left:334px;top:20px;width:288px;font-size:12px;line-height:16px}
.col-feed .section-title{text-align:left;padding-left:78px;margin-top:20px;position:relative}
.col-feed .section-title::before{content:"";position:absolute;left:38px;top:-18px;width:26px;height:26px;border-radius:50%;background:#3d9ad6}
.col-feed h3{font-size:13.5px;margin-top:14px;line-height:17px}
.col-feed p{margin-top:12px}
.col-feed a{color:#1a0dab}
.section-what{position:absolute;left:16px;top:442px;width:614px}
.section-what>p{margin-top:14px;text-align:justify}
.section-what ol{margin:14px 0 0 12px;list-style:none;counter-reset:n}
.section-what li{counter-increment:n;margin-bottom:4px}
.section-what li::before{content:counter(n) ".  ";white-space:pre}
.section-what .btn{margin-top:4px}
.sidebar{position:absolute;left:808px;top:178px;width:246px;font-size:13px;line-height:17px}
.block-head{height:44px;display:flex;align-items:center;gap:14px;padding-left:18px;color:var(--head-text);font-size:17px;font-weight:400;font-variant:small-caps;letter-spacing:.5px;
  background:linear-gradient(var(--btn-top),var(--btn-bottom));border:1px solid var(--btn-edge);border-radius:6px}
.block-head i{width:28px;height:18px;background:#6b2a1c;border-radius:3px;transform:rotate(-14deg)}
.block-list{list-style:none;padding:27px 0 0 20px}
.block-list li{position:relative;padding:12px 0 0 8px;margin-bottom:14px;color:var(--muted)}
.block-list li::before{content:"";position:absolute;left:-4px;top:0;border:3px solid transparent;border-left:4px solid #6a8fb0}
.block-list a{color:var(--link-blue);text-decoration:none}
.resources{position:absolute;top:283px;width:246px}
.resources .block-list{padding-top:26px}
.resources .block-list li{margin-bottom:13px}
.resources .btn{width:156px;margin-left:16px;margin-top:-2px}
.follow{position:absolute;top:635px;width:246px}
.social-links{display:grid;grid-template-columns:1fr 1fr;gap:8px 10px;padding:20px 0 0 18px;font-size:13px}
.social-link{display:flex;align-items:center;gap:6px;color:var(--link-blue);text-decoration:none}
.social-link span{width:14px;height:14px;background:var(--heading-blue);border-radius:2px}
.site-footer{position:absolute;left:0;top:1106px;width:1200px;text-align:center;font-size:11.5px;color:#111}
</style>
</head>
<body>
<nav class="main-nav">
  <a class="nav-item" href="#">Home</a><a class="nav-item" href="#">About</a><a class="nav-item" href="#">Ministries</a>
  <a class="nav-item" href="#">Events</a><a class="nav-item" href="#">Messages</a><a class="nav-item" href="#">Resources</a>
  <a class="nav-item" href="#">Donations</a><a class="nav-item" href="#">Gallery</a><a class="nav-item" href="#">Contact</a>
</nav>

<header>
  <div class="site-emblem" role="img" aria-label="Open bible with a wooden cross"></div>
  <h1 class="site-title">Enter Site Title</h1>
  <div class="site-slogan">Enter Site Slogan</div>
  <div class="site-search">
    <svg width="15" height="15" viewBox="0 0 15 15"><circle cx="7.5" cy="7.5" r="7" fill="#5cbf3a"/><circle cx="6.8" cy="6.8" r="2.6" fill="none" stroke="#fff" stroke-width="1.4"/><line x1="8.7" y1="8.7" x2="11" y2="11" stroke="#fff" stroke-width="1.6"/></svg>
  </div>
</header>

<div class="page-panel"></div>

<main class="content-box">
  <section class="col-who">
    <h2 class="section-title">Who We Are</h2>
    <div class="hero-image" role="img" aria-label="Glowing cross against a blue sky with clouds"></div>
    <h3>Sodales posuere id porta adipiscing sed pretium a donec suscipit.</h3>
    <p>Etiam viverra nisl elementum sed mi suspendisse sagittis curae hendrerit magnis felis et sociosqu lorem vel. Ac erat et purus accumsan nunc.</p>
    <a class="btn" href="#">More Info</a>
  </section>

  <section class="col-feed">
    <h2 class="section-title">Follow Us Chirpline</h2>
    <h3>Metus vivamus egestas volutpat in at libero</h3>
    <p>@kmorrow love all that you do for us</p>
    <p>RT @Lena_pHartley: My favorite little lady on Sunday mornings!!!! @yourchurch<br><a href="#">http://lnk.ex/4kQwR2</a></p>
    <p>RT @Lena_pHartley: My favorite little lady on Sunday mornings!!!! @yourchurch<br><a href="#">http://lnk.ex/4kQwR2</a></p>
    <p>Pastor @danwells raising up a generation begging the glory of God fall! #gracefield #hopehouseva <a href="#">http://lnk.ex/Hv8mZa</a></p>
    <p>this then is how you should pray. #lovemykids #yourchurch #proudjesuslover @ Your Church <a href="#">http://lnk.ex/Rp27Ybd</a></p>
  </section>

  <section class="section-what">
    <h2 class="section-title">What We Do</h2>
    <p>Vel tempus ac posuere eu vivamus ipsum nibh condimentum felis in tristique ut convallis sem id donec fusce. Id nulla sagittis pede ipsum.</p>
    <ol>
      <li>Nisi et leo libero sed. vestibulum pede netus nulla massa diam dui posuere dui pulvinar laoreet.</li>
      <li>Lorem nunc adipiscing. Magna praesent nunc faucibus neque sagittis fermentum enim donec felis nec.</li>
      <li>Et nam praesent luctus. Elit sem nunc blandit quam cras egestas suspendisse nisi posuere ipsum at.</li>
      <li>Nam id malesuada nec. Nunc metus elementum viverra ut fusce nisi et quam aliquam nulla amet amet.</li>
      <li>Nisl tincidunt ipsum. Quis phasellus convallis fames pellentesque quam posuere condimentum quis.</li>
      <li>Viverra sagittis magna. Interdum sed magnis vitae donec nec a nec sapien aliquet ultrices quis ut.</li>
      <li>Ultricies metus dis ac. Mi in primis fusce ac hendrerit at nam quis neque ipsum libero nec rhoncus.</li>
      <li>Feugiat tempus ipsum. Ac ut lectus libero leo egestas justo eros hendrerit donec sit turpis ac.</li>
    </ol>
    <a class="btn" href="#">More Info</a>
  </section>
</main>

<aside class="sidebar">
  <section class="events">
    <h2 class="block-head"><i></i>Events</h2>
    <ul class="block-list">
      <li>Jan. 7 - 11, 2013<br><a href="#">Leaders in the<br>Shared Table Gathering</a><br>Brookhaven, OH</li>
      <li>Jan. 21 - 25, 2013<br><a href="#">Faithful Steps<br>Ministry Summit</a><br>Harbor Point, Maine</li>
    </ul>
  </section>
  <section class="resources">
    <h2 class="block-head"><i></i>Resources</h2>
    <ul class="block-list">
      <li><a href="#">Cedar Hill study guide</a><br>from <a href="#">Riverstone Mission Agency</a></li>
      <li><a href="#">Quiet Streets, Open Doors:<br>Serving Our Neighbors in<br>Hard Times</a><br>from <a href="#">Riverstone Mission Agency</a></li>
      <li><a href="#">Prayer Card - Tomas Ridley and<br>Mara Ellison</a><br>from <a href="#">Riverstone Mission Agency</a></li>
    </ul>
    <a class="btn" href="#">View All Resources</a>
  </section>
  <section class="follow">
    <h2 class="block-head"><i></i>Follow Us</h2>
    <div class="social-links">
      <a class="social-link" href="#"><span></span>Friendwall</a>
      <a class="social-link" href="#"><span></span>Linkhub</a>
      <a class="social-link" href="#"><span></span>Chirpline</a>
      <a class="social-link" href="#"><span></span>Streamtube</a>
    </div>
  </section>
</aside>

<footer class="site-footer">Copyright © 2012. All Rights Reserved.</footer>
</body>
</html>
```